Brightmere Pictures Business Card

Hello,

i would like to have a dynamic, creative but tasteful card, colour used, front and back. I have attached a sample card that I liked very much from another individual to give you an idea of the theme/approach, but not colour. Ideally the graphic elements of the Brightmere Logo are brought into the design.

Target Market(s)

North America

Industry/Entity Type

Film Production

Contact Information for Business Card

Nadia Pellwick
President/Founder
Brightmere Pictures Inc.
403 555 2917
nadia@brightmerepictures.tv

Font styles to use
Sans Serif

Colors
6b449b
5c5c5c
fdfdfd
000000

Requirements
Must have
• Logo, name, Company name, email and cell number. no Address line to be included.
Should not have
• any unrelated GFX elements, serif fonts

```html
<!DOCTYPE html>
<html lang="en">
<head>
<meta charset="utf-8">
<title>Brightmere Pictures Business Card</title>
<link href="https://fonts.googleapis.com/css2?family=Jost:wght@400;500&display=swap" rel="stylesheet">
<style>
  :root {
    --brand-purple: #6b449b;
    --purple-deep: #4a2678;
    --purple-bright: #5b2d95;
    --ink-grey: #5c5c5c;
    --paper: #fdfdfd;
    --paper-shade: #e9e9e9;
    --name-silver: #d6d6d6;
    --backdrop: #2b2b2d;
  }
  * { box-sizing: border-box; margin: 0; padding: 0; }
  html, body { width: 1200px; height: 900px; overflow: hidden; }
  body {
    background: var(--backdrop);
    font-family: "Jost", "Helvetica Neue", Arial, sans-serif;
    display: flex;
    flex-direction: column;
    align-items: center;
    justify-content: center;
    gap: 52px;
  }
  .card {
    width: 630px;
    height: 360px;
    border-radius: 26px;
    position: relative;
    overflow: hidden;
    box-shadow: 0 14px 30px rgba(0,0,0,0.45);
  }
  /* Front */
  .card--front {
    background: radial-gradient(ellipse at 55% 55%, var(--paper) 40%, var(--paper-shade) 100%);
  }
  .company-name {
    position: absolute;
    top: 48px;
    right: 48px;
    font-size: 22px;
    letter-spacing: 0.08em;
    text-transform: uppercase;
    color: var(--ink-grey);
  }
  .company-name .accent { color: var(--brand-purple); }
  .contact-block {
    position: absolute;
    left: 50px;
    bottom: 58px;
  }
  .person-name {
    font-size: 22px;
    font-weight: 500;
    letter-spacing: 0.06em;
    text-transform: uppercase;
    color: var(--brand-purple);
    line-height: 1.1;
  }
  .person-title {
    font-size: 17px;
    color: var(--ink-grey);
    margin-bottom: 16px;
  }
  .contact-line {
    display: flex;
    align-items: center;
    gap: 10px;
    font-size: 17px;
    color: var(--ink-grey);
    line-height: 1.45;
  }
  .contact-line svg { width: 14px; height: 14px; flex: none; }
  /* Back */
  .card--back {
    background: linear-gradient(135deg, var(--purple-deep) 0%, var(--purple-bright) 55%, var(--purple-deep) 100%);
    display: flex;
    align-items: center;
    justify-content: center;
  }
  .brand-name {
    font-size: 44px;
    font-weight: 500;
    color: var(--name-silver);
    line-height: 1;
  }
</style>
</head>
<body>

  <section class="card card--front" aria-label="Card front">
    <p class="company-name">Brightmere <span class="accent">Pictures Inc.</span></p>
    <div class="contact-block">
      <p class="person-name">Nadia Pellwick</p>
      <p class="person-title">President/Founder</p>
      <p class="contact-line">
        <svg viewBox="0 0 16 16" aria-hidden="true"><path d="M4 1.5c.6 0 1 .4 1.2.9l.8 2.3c.1.5 0 1-.4 1.3L4.6 6.8c.8 1.8 2.2 3.2 4 4l.8-1c.3-.4.8-.5 1.3-.4l2.3.8c.5.2.9.6.9 1.2v1.8c0 .8-.7 1.4-1.5 1.3C6.6 13.9 2.1 9.4 1.5 3.5 1.4 2.7 2 2 2.8 2z" fill="var(--brand-purple)"/></svg>
        403 555 2917
      </p>
      <p class="contact-line">
        <svg viewBox="0 0 16 16" aria-hidden="true"><rect x="1.5" y="3.5" width="13" height="9" rx="1" fill="none" stroke="var(--brand-purple)" stroke-width="1.6"/><path d="M2 4.5l6 4.5 6-4.5" fill="none" stroke="var(--brand-purple)" stroke-width="1.6"/></svg>
        nadia@brightmerepictures.tv
      </p>
    </div>
  </section>

  <section class="card card--back" aria-label="Card back">
    <p class="brand-name">Brightmere Pictures</p>
  </section>

</body>
</html>
```